Goat's Milk Soap

International product development company seeking designs for the following soap label:

Hand crafted in Mt Berryman QLD Australia, Lockyer Valley
Second Generation Goat Farmers
Soap is hand made in appearance but gives an instant soothing feel when used
High in Vegetable oils and pure fresh goats milk (no powders used)
Give the emotional feel of Quality and Hand crafted
Label must stimulate an emotional response visually
Label must deliver to the customer anticipation for use.
Would anticipate that the label will be produced on a matte finish brown paper label or similar.

Logo should be no larger than 50mm x 50mm
Label should measure around 120mm x 70mm

It Company

```html
<!DOCTYPE html>
<html lang="en">
<head>
<meta charset="utf-8">
<title>Goat Milk Soap Label</title>
<link rel="stylesheet" href="https://fonts.googleapis.com/css2?family=Cabin:wght@500&family=Alfa+Slab+One&family=Open+Sans:wght@400&display=swap">
<style>
  :root {
    --purple: #8b2479;
    --purple-deep: #6e1a60;
    --gold: #fbbf00;
    --gold-soft: #f7c64a;
    --lilac: #d6b3d4;
    --ink: #111111;
    --paper: #ffffff;
  }
  html, body {
    margin: 0;
    padding: 0;
    width: 697px;
    height: 1200px;
    overflow: hidden;
    background: var(--paper);
  }
  .sheet {
    position: relative;
    width: 697px;
    height: 1200px;
  }
  .spec {
    position: absolute;
    font-family: "Open Sans", sans-serif;
    font-size: 31px;
    color: var(--ink);
    line-height: 1;
    text-align: center;
    z-index: 2;
  }
  .spec--title { left: 0; width: 655px; top: 6px; }
  .spec--width { left: 0; width: 655px; top: 45px; }
  .spec--height {
    left: 674px;
    top: 645px;
    transform: translate(-50%, -50%) rotate(90deg);
    white-space: nowrap;
  }
  .label {
    position: absolute;
    left: 2px;
    top: 88px;
    width: 647px;
    height: 1110px;
    border: 1px solid var(--ink);
    box-sizing: border-box;
    overflow: hidden;
    background: var(--paper);
  }
  .label__art {
    position: absolute;
    inset: 0;
  }
  .emblem-art { fill: url(#emblemFill); }
  .splash-art { fill: url(#splashFill); }
  .product-name {
    position: absolute;
    left: 88px;
    top: 522px;
    width: 457px;
    height: 66px;
    background: var(--gold);
    display: flex;
    align-items: center;
    justify-content: center;
    gap: 8px;
    font-size: 54px;
    color: var(--paper);
    text-shadow: 3px 3px 0 var(--purple-deep);
    line-height: 1;
  }
  .product-name__word { font-family: "Cabin", sans-serif; font-weight: 500; }
  .product-name__word--strong { font-family: "Alfa Slab One", serif; font-size: 50px; }
</style>
</head>
<body>
<div class="sheet">
  <div class="spec spec--title">Option 4</div>
  <div class="spec spec--width">70mm</div>
  <div class="spec spec--height">120mm</div>

  <div class="label">
    <svg class="label__art" width="645" height="1108" viewBox="0 0 645 1108" xmlns="http://www.w3.org/2000/svg">
      <defs>
        <radialGradient id="emblemFill" cx="50%" cy="45%" r="60%">
          <stop offset="0%" stop-color="#c99bc1"/>
          <stop offset="100%" stop-color="#8b2479"/>
        </radialGradient>
        <linearGradient id="splashFill" x1="0" y1="0" x2="0" y2="1">
          <stop offset="0%" stop-color="#f2f2ee"/>
          <stop offset="100%" stop-color="#dcdcd4"/>
        </linearGradient>
      </defs>

      <circle cx="316" cy="314" r="190" fill="none" stroke="var(--gold-soft)" stroke-width="2" stroke-dasharray="7 5"/>
      <circle cx="316" cy="314" r="175" fill="var(--gold)"/>
      <circle cx="316" cy="314" r="155" fill="var(--paper)"/>
      <circle class="emblem-art" cx="316" cy="314" r="151" role="img" aria-label="Cartoon sheep mascot waving inside a purple sunburst circle"/>

      <path d="M0,830 C100,815 200,890 300,886 C430,880 540,858 645,864 L645,1108 L0,1108 Z" fill="var(--purple)"/>
      <path d="M0,800 C110,745 220,755 330,805 C440,850 540,870 645,876 L645,888 C540,884 440,866 330,822 C220,778 110,772 0,828 Z" fill="var(--lilac)"/>
      <path d="M0,742 C110,700 220,705 330,755 C440,808 540,842 645,858 L645,870 C540,858 440,830 330,782 C220,735 110,735 0,774 Z" fill="var(--gold)"/>

      <rect class="splash-art" x="200" y="815" width="400" height="245" rx="24" role="img" aria-label="Splash of fresh goat's milk"/>
    </svg>

    <div class="product-name">
      <span class="product-name__word">Goat</span>
      <span class="product-name__word product-name__word--strong">Milk</span>
      <span class="product-name__word">Soap</span>
    </div>
  </div>
</div>
</body>
</html>
```